Brambys Burgers and Tacos needs a new menu board design

We are a fast casual restaurant that sells burgers, tacos, wraps and other items. We have a California feel, sleek and modern, décor has photos of people like Pelliver, Marsk, Dorvale. Song list varies from Copper Wheels, Lantern Moth, Quivers, Halloway Ferrystone etc... Our main goal for this project is to clean up the look of our menu boards...make them easier to read and more reflective of the style of the restaurant. We also want to feature our combos which are our high profit items...think they should take up 30 to 40% of the space.

We have t-shirts that say "Don't Worry Be Hippy", "Hold On Brighter Days", "Make Tacos Not War".

There is potential for other projects such as outdoor menu panels, paper menus, promotional items. I am attaching a layout of the menu panels as they appear now with dimensions. Also photos of the restaurant. We are not planning to use these same panels so please don't design around them...come up with your own ideas on this....there is a slightly curved background. We have a really good sign person that can customize if need be.

We have had this menu for a long time and it needs to be clean and sleek.

Target Market(s)

teenagers to 40+

Industry/Entity Type

Restaurant

Requirements
Must have
• Clean readable headers

```html
<!DOCTYPE html>
<html lang="en">
<head>
<meta charset="utf-8">
<title>Combos Menu Board</title>
<link rel="stylesheet" href="https://fonts.googleapis.com/css2?family=Yellowtail&family=Cabin+Condensed:wght@500;600&display=swap">
<style>
  :root {
    --stone-light: #8a8d87;
    --stone-mid: #767973;
    --stone-dark: #62655f;
    --board: #323331;
    --board-edge: #3a3b39;
    --white: #ffffff;
    --lime: #c6f000;
    --gold: #f2cf14;
  }
  * { margin: 0; padding: 0; box-sizing: border-box; }
  html, body { width: 1155px; height: 1200px; overflow: hidden; }
  body {
    position: relative;
    background:
      radial-gradient(ellipse at 20% 15%, var(--stone-light) 0%, transparent 55%),
      radial-gradient(ellipse at 80% 70%, var(--stone-light) 0%, transparent 50%),
      radial-gradient(ellipse at 55% 95%, var(--stone-dark) 0%, transparent 45%),
      var(--stone-mid);
    font-family: "Cabin Condensed", "Arial Narrow", sans-serif;
    color: var(--white);
  }
  .menu-title {
    position: absolute;
    top: 8px;
    left: 0;
    width: 1155px;
    text-align: center;
    font-family: "Yellowtail", cursive;
    font-weight: 400;
    font-size: 200px;
    line-height: 230px;
    color: var(--white);
    text-shadow: -6px 5px 0 var(--lime);
  }
  .column-divider {
    position: absolute;
    left: 577px;
    top: 246px;
    width: 3px;
    height: 714px;
    background: var(--white);
  }
  .combo {
    position: absolute;
    width: 434px;
    height: 148px;
    background: linear-gradient(135deg, var(--board-edge), var(--board) 60%);
  }
  .combo-number {
    position: absolute;
    left: 5px;
    top: 10px;
    font-family: Arial, Helvetica, sans-serif;
    font-size: 34px;
    line-height: 1;
    color: var(--gold);
  }
  .combo-name {
    position: absolute;
    left: 55px;
    top: 6px;
    white-space: nowrap;
    line-height: 1;
  }
  .combo-name .brand {
    font-family: "Yellowtail", cursive;
    font-size: 40px;
    margin-right: 10px;
  }
  .combo-name .item {
    font-family: "Cabin Condensed", "Arial Narrow", sans-serif;
    font-weight: 600;
    font-size: 33px;
  }
  .combo-sides {
    position: absolute;
    left: 0;
    width: 444px;
    top: 79px;
    text-align: center;
    font-weight: 600;
    font-size: 21px;
    line-height: 1;
  }
  .combo-extra {
    position: absolute;
    left: 0;
    width: 444px;
    top: 100px;
    text-align: center;
    font-weight: 500;
    font-size: 13px;
    line-height: 1;
  }
  .combo-addon {
    position: absolute;
    left: 3px;
    bottom: 3px;
    font-weight: 500;
    font-size: 13px;
    line-height: 1;
  }
  .combo-addon .addon-price {
    font-family: Arial, Helvetica, sans-serif;
    font-size: 12px;
    color: var(--gold);
  }
  .combo-price {
    position: absolute;
    right: 12px;
    bottom: 9px;
    font-family: Arial, Helvetica, sans-serif;
    font-size: 30px;
    line-height: 1;
    color: var(--gold);
  }
  .combo-price sup {
    font-size: 18px;
    vertical-align: 11px;
  }
  .left  { left: 76px; }
  .right { left: 638px; }
  .row-1 { top: 265px; }
  .row-2 { top: 442px; }
  .row-3 { top: 619px; }
  .row-4 { top: 795px; }
  .combo-feature { left: 361px; top: 992px; }
</style>
</head>
<body>
  <h1 class="menu-title">Combos</h1>
  <div class="column-divider"></div>

  <section class="combo left row-1">
    <span class="combo-number">1</span>
    <h2 class="combo-name"><span class="brand">Bramby</span><span class="item">Cheese burger</span></h2>
    <p class="combo-sides">Mixed fries - 20oz Drink</p>
    <p class="combo-extra">add grilled onions FREE!</p>
    <p class="combo-addon">add bacon <span class="addon-price">99¢</span></p>
    <p class="combo-price">8<sup>69</sup></p>
  </section>
  <section class="combo right row-1">
    <span class="combo-number">2</span>
    <h2 class="combo-name"><span class="brand">Bramby</span><span class="item">Cheese burger</span></h2>
    <p class="combo-sides">Mixed fries - 20oz Drink</p>
    <p class="combo-extra">add grilled onions FREE!</p>
    <p class="combo-addon">add bacon <span class="addon-price">99¢</span></p>
    <p class="combo-price">8<sup>69</sup></p>
  </section>
  <section class="combo left row-2">
    <span class="combo-number">3</span>
    <h2 class="combo-name"><span class="brand">Bramby</span><span class="item">Cheese burger</span></h2>
    <p class="combo-sides">Mixed fries - 20oz Drink</p>
    <p class="combo-extra">add grilled onions FREE!</p>
    <p class="combo-addon">add bacon <span class="addon-price">99¢</span></p>
    <p class="combo-price">8<sup>69</sup></p>
  </section>
  <section class="combo right row-2">
    <span class="combo-number">4</span>
    <h2 class="combo-name"><span class="brand">Bramby</span><span class="item">Cheese burger</span></h2>
    <p class="combo-sides">Mixed fries - 20oz Drink</p>
    <p class="combo-extra">add grilled onions FREE!</p>
    <p class="combo-addon">add bacon <span class="addon-price">99¢</span></p>
    <p class="combo-price">8<sup>69</sup></p>
  </section>
  <section class="combo left row-3">
    <span class="combo-number">5</span>
    <h2 class="combo-name"><span class="brand">Bramby</span><span class="item">Cheese burger</span></h2>
    <p class="combo-sides">Mixed fries - 20oz Drink</p>
    <p class="combo-extra">add grilled onions FREE!</p>
    <p class="combo-addon">add bacon <span class="addon-price">99¢</span></p>
    <p class="combo-price">8<sup>69</sup></p>
  </section>
  <section class="combo right row-3">
    <span class="combo-number">6</span>
    <h2 class="combo-name"><span class="brand">Bramby</span><span class="item">Cheese burger</span></h2>
    <p class="combo-sides">Mixed fries - 20oz Drink</p>
    <p class="combo-extra">add grilled onions FREE!</p>
    <p class="combo-addon">add bacon <span class="addon-price">99¢</span></p>
    <p class="combo-price">8<sup>69</sup></p>
  </section>
  <section class="combo left row-4">
    <span class="combo-number">7</span>
    <h2 class="combo-name"><span class="brand">Bramby</span><span class="item">Cheese burger</span></h2>
    <p class="combo-sides">Mixed fries - 20oz Drink</p>
    <p class="combo-extra">add grilled onions FREE!</p>
    <p class="combo-addon">add bacon <span class="addon-price">99¢</span></p>
    <p class="combo-price">8<sup>69</sup></p>
  </section>
  <section class="combo right row-4">
    <span class="combo-number">8</span>
    <h2 class="combo-name"><span class="brand">Bramby</span><span class="item">Cheese burger</span></h2>
    <p class="combo-sides">Mixed fries - 20oz Drink</p>
    <p class="combo-extra">add grilled onions FREE!</p>
    <p class="combo-addon">add bacon <span class="addon-price">99¢</span></p>
    <p class="combo-price">8<sup>69</sup></p>
  </section>
  <section class="combo combo-feature">
    <span class="combo-number">9</span>
    <h2 class="combo-name"><span class="brand">Bramby</span><span class="item">Cheese burger</span></h2>
    <p class="combo-sides">Mixed fries - 20oz Drink</p>
    <p class="combo-extra">add grilled onions FREE!</p>
    <p class="combo-addon">add bacon <span class="addon-price">99¢</span></p>
    <p class="combo-price">8<sup>69</sup></p>
  </section>
</body>
</html>
```